Portal Panel Medic need professional looking business card printed on plastic, Commericial, Industri

We are family owned and operated garage door company in Indianapolis, Indiana. We sale service and install dock equipment, doors, operators. We are looking to expand our commercial/ industrial division. We also service all residential doors and operators. We are looking for a business that stands out of the crowd. We are committed to have the best customer service in the industry.

Target Market(s)

National and local general contractors, National/ Corpate service accounts,

Industry/Entity Type

Business Service

Contact Information for Business Card

To be printed on plastic stock

Font styles to use
Sans Serif

Colors
ffffff
f04a50
ec1f27

Requirements
Must have
• Name, website,email, phone number, position.
Nice to have
• A standout professional design

```html
<!DOCTYPE html>
<html lang="en">
<head>
<meta charset="utf-8">
<title>Portal Panel Medic — Business Card</title>
<link rel="stylesheet" href="https://fonts.googleapis.com/css2?family=Open+Sans:wght@400;600;700;800&display=swap">
<style>
  :root {
    --white: #ffffff;
    --coral: #f04a50;
    --red: #ec1f27;
    --red-deep: #c8161d;
    --ink: #1c1c1c;
    --stage: #e9e6e1;
    --art-light: #d9d4cc;
    --art-mid: #a89484;
  }
  * { box-sizing: border-box; margin: 0; padding: 0; }
  html, body {
    width: 1200px; height: 1024px; overflow: hidden;
    background: var(--stage);
    font-family: "Open Sans", Arial, sans-serif;
  }
  .sheet {
    width: 1200px; height: 1024px;
    display: flex; flex-direction: column; align-items: center; justify-content: center;
    gap: 64px;
  }
  .card {
    width: 700px; height: 400px;
    border-radius: 6px;
    box-shadow: 0 10px 28px rgba(0,0,0,.18);
    position: relative; overflow: hidden;
  }

  /* Front */
  .card-front { background: var(--white); display: flex; }
  .mascot-art {
    width: 300px; height: 100%;
    background: radial-gradient(ellipse at 55% 55%, var(--art-light) 0%, var(--art-mid) 65%, var(--white) 100%);
  }
  .front-info {
    flex: 1; padding: 44px 40px 0 24px;
    display: flex; flex-direction: column;
  }
  .brand-name {
    font-weight: 800; font-size: 44px; line-height: 1.02;
    color: var(--red); text-transform: uppercase; letter-spacing: -0.5px;
  }
  .person-name {
    margin-top: 30px;
    font-weight: 800; font-size: 24px; color: var(--red); text-transform: uppercase;
  }
  .person-role { font-weight: 700; font-size: 17px; color: var(--ink); margin-top: 2px; }
  .contact-list { list-style: none; margin-top: 22px; display: flex; flex-direction: column; gap: 10px; }
  .contact-item { display: flex; align-items: center; gap: 12px; font-size: 17px; color: var(--ink); }
  .contact-icon { width: 24px; height: 24px; flex: none; }

  /* Back */
  .card-back {
    background: linear-gradient(135deg, var(--coral) 0%, var(--red) 55%, var(--red-deep) 100%);
    display: flex; align-items: center; justify-content: center;
  }
  .back-brand {
    font-weight: 800; font-size: 52px; line-height: 1.02; text-align: center;
    color: var(--white); text-transform: uppercase;
  }
  .back-web {
    position: absolute; left: 34px; bottom: 26px;
    font-size: 17px; color: var(--white);
  }
</style>
</head>
<body>
<main class="sheet">
  <section class="card card-front">
    <div class="mascot-art" role="img" aria-label="Cartoon illustration of a door repair doctor with stethoscope, seated"></div>
    <div class="front-info">
      <h1 class="brand-name">Portal<br>Panel Medic</h1>
      <p class="person-name">Marcus Hale</p>
      <p class="person-role">Position</p>
      <ul class="contact-list">
        <li class="contact-item">
          <svg class="contact-icon" viewBox="0 0 24 24" aria-hidden="true"><circle cx="12" cy="12" r="12" fill="var(--red)"/><path d="M8 6.5c.6-.4 1.3-.3 1.6.3l1 1.8c.3.5.1 1.1-.3 1.4l-.7.5c.6 1.3 1.6 2.3 2.9 2.9l.5-.7c.3-.4.9-.6 1.4-.3l1.8 1c.6.3.7 1 .3 1.6l-.7.9c-.5.6-1.4.8-2.1.5-3-1.3-5.3-3.6-6.6-6.6-.3-.7-.1-1.6.5-2.1z" fill="var(--white)"/></svg>
          317-555-0148
        </li>
        <li class="contact-item">
          <svg class="contact-icon" viewBox="0 0 24 24" aria-hidden="true"><rect x="1" y="1" width="22" height="22" rx="3" fill="var(--red)"/><rect x="5.5" y="7.5" width="13" height="9" fill="none" stroke="var(--white)" stroke-width="1.5"/><path d="M5.5 7.5l6.5 5 6.5-5" fill="none" stroke="var(--white)" stroke-width="1.5"/></svg>
          marcus@portalpanelmedic.com
        </li>
        <li class="contact-item">
          <svg class="contact-icon" viewBox="0 0 24 24" aria-hidden="true"><circle cx="12" cy="12" r="12" fill="var(--red)"/><circle cx="12" cy="12" r="6.5" fill="none" stroke="var(--white)" stroke-width="1.4"/><ellipse cx="12" cy="12" rx="2.8" ry="6.5" fill="none" stroke="var(--white)" stroke-width="1.2"/><line x1="5.5" y1="12" x2="18.5" y2="12" stroke="var(--white)" stroke-width="1.2"/></svg>
          www.portalpanelmedic.com
        </li>
      </ul>
    </div>
  </section>

  <section class="card card-back">
    <h2 class="back-brand">Portal<br>Panel Medic</h2>
    <p class="back-web">www.portalpanelmedic.com</p>
  </section>
</main>
</body>
</html>
```